Wine label Design

We are looking to develop an elegant contemporary Chilean design; for a new Wine Brand TORVANE to be sold in Chinese Market.
We would like to see designs that are a fine balance between having a traditional design that can offer quality reassurance and being distinctive enough to stand out on crowded shelves. The final design should be easy-to-remember and communicate Quality, Tradition and have a conection with Chile.

Target Market(s)

Urban Chinese between 25 to 40 yo

Requirements
Must have
• Paper label
Information on Front label : Grape (example Cabernet sauvignon) / Vintage (ex 2010) / Wine of Chile
Bottle shape is given (see attached)
Nice to have
• An element of uniqueness, easy to recall the brand
Red and Gold Color are appreciated by the Target
Should not have
• White background
Number 4 is considered death, should not be included on the design

```html
<!DOCTYPE html>
<html lang="en">
<head>
<meta charset="utf-8">
<title>TORVANE Vintage Cabernet Sauvignon – Wine Label</title>
<link href="https://fonts.googleapis.com/css2?family=Cinzel:wght@400;600&family=Great+Vibes&family=Cormorant+Garamond:wght@500&display=swap" rel="stylesheet">
<style>
  :root {
    --backdrop-light: #ffffff;
    --backdrop-edge: #d9d9d9;
    --label-gold: #d6a232;
    --label-body: #2a2a2a;
    --label-band: #2f2f2f;
    --foliage-tone: #363636;
    --text-gold: #c9952c;
    --text-silver: #e4e4e4;
  }
  * { margin: 0; padding: 0; box-sizing: border-box; }
  html, body { width: 1200px; height: 1000px; overflow: hidden; }
  body {
    position: relative;
    background: radial-gradient(ellipse at center, var(--backdrop-light) 55%, var(--backdrop-edge) 100%);
    font-family: "Cinzel", serif;
  }
  .label-shape { position: absolute; left: 0; top: 0; width: 1200px; height: 1000px; }
  .label-text {
    position: absolute; left: 0; width: 1200px;
    text-align: center; white-space: nowrap;
  }
  .origin {
    top: 72px; font-size: 33px; letter-spacing: 1px;
    color: var(--text-gold); font-family: "Cinzel", serif;
  }
  .brand-name {
    top: 228px; font-size: 104px; font-weight: 600; letter-spacing: 6px;
    color: var(--text-gold); font-family: "Cinzel", serif;
  }
  .range-name {
    top: 452px; font-size: 122px; left: -14px;
    color: var(--text-gold); font-family: "Great Vibes", cursive;
  }
  .grape-variety {
    top: 622px; font-size: 54px; letter-spacing: 2px;
    color: var(--text-silver); font-family: "Cinzel", serif;
  }
  .vintage-year {
    top: 722px; font-size: 60px;
    color: var(--text-gold); font-family: "Cormorant Garamond", serif; font-weight: 500;
  }
</style>
</head>
<body>
  <svg class="label-shape" viewBox="0 0 1200 1000" xmlns="http://www.w3.org/2000/svg">
    <defs>
      <linearGradient id="rule-fade" x1="0" x2="1">
        <stop offset="0" stop-color="#c9952c" stop-opacity="0"/>
        <stop offset="0.5" stop-color="#c9952c" stop-opacity="1"/>
        <stop offset="1" stop-color="#c9952c" stop-opacity="0"/>
      </linearGradient>
      <radialGradient id="foliage-glow" cx="0.5" cy="0.5" r="0.5">
        <stop offset="0" stop-color="#3a3a3a"/>
        <stop offset="1" stop-color="#2a2a2a" stop-opacity="0"/>
      </radialGradient>
    </defs>

    <path class="label-frame" fill="var(--label-gold)"
      d="M332,23 H868 A90,90 0 0 0 958,113 V885 A90,90 0 0 0 868,975 H332 A90,90 0 0 0 242,885 V113 A90,90 0 0 0 332,23 Z"/>
    <path class="label-body" fill="var(--label-body)"
      d="M340,31 H860 A98,98 0 0 0 950,121 V877 A98,98 0 0 0 860,967 H340 A98,98 0 0 0 250,877 V121 A98,98 0 0 0 340,31 Z"/>

    <rect role="img" aria-label="Faint Andean triangle pattern band" x="250" y="112" width="700" height="72" fill="var(--label-band)"/>
    <rect role="img" aria-label="Faint Andean triangle pattern band" x="250" y="805" width="700" height="80" fill="var(--label-band)"/>
    <ellipse role="img" aria-label="Faint illustration of vine leaves and a grape cluster" cx="600" cy="560" rx="330" ry="330" fill="url(#foliage-glow)"/>

    <g class="origin-rules" stroke="var(--text-gold)" stroke-width="2">
      <line x1="405" y1="95" x2="428" y2="95"/>
      <line x1="778" y1="95" x2="800" y2="95"/>
    </g>
    <g class="variety-rules" stroke="url(#rule-fade)" stroke-width="2">
      <line x1="280" y1="609" x2="920" y2="609"/>
      <line x1="280" y1="696" x2="920" y2="696"/>
    </g>
    <g class="year-rules" stroke="var(--text-gold)" stroke-width="2">
      <line x1="465" y1="752" x2="525" y2="752"/>
      <line x1="680" y1="752" x2="742" y2="752"/>
    </g>
  </svg>

  <div class="label-text origin">WINE OF CHILE</div>
  <div class="label-text brand-name">TORVANE</div>
  <div class="label-text range-name">Vintage</div>
  <div class="label-text grape-variety">Cabernet Sauvignon</div>
  <div class="label-text vintage-year">2010</div>
</body>
</html>
```